We are an integrated facilities management company.

We aggregate everything related to facilities maintenance. Repair-replacement of equipment and facility space materials from:
Asset gathering and tracking.
Vendor screening, contracting and management.
Service requirement development.
Work order processing and management.
Invoice reconciliation.
Vendor payment.
Reporting.
Capital equipment bids and project management.

Target Market(s)

Retail, hospitality, multi-family housing, long term healthcare.

Industry/Entity Type

Maintenance

Contact Information for Business Card

Professional and bold look. (see logo zip file)

Colors
3377b5
85abd2
cedeed

Requirements
Must have
• N/A
Nice to have
• N/A
Should not have
• N/A

```html
<!DOCTYPE html>
<html lang="en">
<head>
<meta charset="UTF-8">
<title>Northvale Facility Partners – Business Card</title>
<link href="https://fonts.googleapis.com/css2?family=Montserrat:wght@400;500;600;700&display=swap" rel="stylesheet">
<style>
  :root {
    --brand-blue: #3377b5;
    --brand-sky: #85abd2;
    --brand-mist: #cedeed;
    --ink: #3a3f45;
    --ink-soft: #6b7179;
    --card-dark: #2b2c2e;
    --card-light: #ffffff;
    --backdrop: #e4e5e7;
  }
  * { box-sizing: border-box; margin: 0; padding: 0; }
  html, body { width: 1200px; height: 800px; overflow: hidden; }
  body {
    background: var(--backdrop);
    font-family: "Montserrat", sans-serif;
    color: var(--ink);
    position: relative;
  }
  .card {
    position: absolute;
    top: 251px;
    width: 525px;
    height: 300px;
    border-radius: 3px;
    box-shadow: 0 10px 28px rgba(0,0,0,0.18);
    overflow: hidden;
  }
  .card--front { left: 50px; background: var(--card-light); border-left: 6px solid var(--brand-blue); }
  .card--back { left: 625px; background: var(--card-dark); border-bottom: 3px solid var(--brand-blue); }

  .wordmark { display: flex; align-items: center; gap: 10px; }
  .wordmark__square { width: 14px; height: 14px; background: var(--brand-blue); flex: none; }
  .wordmark__name { font-weight: 700; color: var(--brand-blue); letter-spacing: 0.5px; text-transform: uppercase; }
  .tagline { font-weight: 500; color: var(--ink-soft); letter-spacing: 3px; text-transform: uppercase; }

  .card--front .wordmark { position: absolute; left: 34px; top: 40px; }
  .card--front .wordmark__name { font-size: 17px; }
  .card--front .tagline { position: absolute; left: 58px; top: 66px; font-size: 8px; }

  .identity { position: absolute; right: 36px; top: 132px; text-align: right; }
  .identity__name { font-size: 19px; font-weight: 700; color: var(--brand-blue); letter-spacing: 0.5px; }
  .identity__title { font-size: 11px; font-weight: 700; color: var(--ink); letter-spacing: 1px; margin-top: 2px; }

  .divider { position: absolute; left: 34px; right: 36px; top: 190px; height: 1px; background: var(--brand-blue); }

  .contact { position: absolute; top: 206px; font-size: 11.5px; line-height: 1.7; color: var(--ink); }
  .contact--address { left: 34px; }
  .contact--phones { left: 215px; }
  .contact--web { right: 36px; }
  .contact__row { display: flex; align-items: center; gap: 7px; }
  .contact__row svg { width: 11px; height: 11px; flex: none; }

  .card--back .lockup { position: absolute; left: 0; right: 0; top: 118px; text-align: center; }
  .card--back .wordmark { justify-content: center; }
  .card--back .wordmark__square { width: 22px; height: 22px; }
  .card--back .wordmark__name { font-size: 26px; color: var(--brand-sky); }
  .card--back .tagline { display: block; margin-top: 10px; font-size: 10px; color: #8a8e94; letter-spacing: 4px; }
</style>
</head>
<body>
  <section class="card card--front" aria-label="Business card front">
    <div class="wordmark">
      <span class="wordmark__square"></span>
      <span class="wordmark__name">Northvale Facility Partners</span>
    </div>
    <span class="tagline">Maintain • Repair • Replace</span>

    <div class="identity">
      <p class="identity__name">DANIEL CARTER</p>
      <p class="identity__title">PRESIDENT</p>
    </div>

    <div class="divider"></div>

    <address class="contact contact--address" style="font-style:normal">
      412 Birchwood Court<br>
      Fairbanks, Alaska 99712
    </address>

    <div class="contact contact--phones">
      <div class="contact__row">
        <svg viewBox="0 0 12 12" aria-hidden="true"><path d="M2.5 1h2l1 3-1.3 1a7 7 0 0 0 2.8 2.8l1-1.3 3 1v2a1 1 0 0 1-1 1A10 10 0 0 1 1.5 2a1 1 0 0 1 1-1z" fill="var(--brand-blue)"/></svg>
        <span>555-204-7731</span>
      </div>
      <div class="contact__row">
        <svg viewBox="0 0 12 12" aria-hidden="true"><rect x="3" y="0.8" width="6" height="10.4" rx="1.2" fill="none" stroke="var(--brand-blue)" stroke-width="1.4"/></svg>
        <span>555-318-6642</span>
      </div>
    </div>

    <div class="contact contact--web">
      <div class="contact__row">
        <svg viewBox="0 0 12 12" aria-hidden="true"><rect x="0.5" y="2" width="11" height="8" rx="1" fill="var(--brand-blue)"/><path d="M1 2.8l5 3.6 5-3.6" fill="none" stroke="#fff" stroke-width="1"/></svg>
        <span>hello@northvalefp.com</span>
      </div>
      <div class="contact__row">
        <svg viewBox="0 0 12 12" aria-hidden="true"><circle cx="6" cy="6" r="5.5" fill="var(--brand-blue)"/><path d="M0.8 6h10.4M6 0.5c-2.4 2.8-2.4 8.2 0 11M6 0.5c2.4 2.8 2.4 8.2 0 11" fill="none" stroke="#fff" stroke-width="0.8"/></svg>
        <span>www.northvalefp.com</span>
      </div>
    </div>
  </section>

  <section class="card card--back" aria-label="Business card back">
    <div class="lockup">
      <div class="wordmark">
        <span class="wordmark__square"></span>
        <span class="wordmark__name">Northvale Facility Partners</span>
      </div>
      <span class="tagline">Maintain • Repair • Replace</span>
    </div>
  </section>
</body>
</html>
```